Roofing Business needs a modern trade show booth design

Our booth is going to be a 10x10 area. we would like a back drop with two roll up banner on the sides. we would also like to have a rectangle table with our design on it.like this one https://www.flagmorrow.ca/fabric-pop-up-booth-square/p
our website is www.pelwickbuilders.ca we are updating our logo. the new one is attached. We would like one of the banners to have a vacation give away I have attached examples. Our Main Focus is roofing and eavestrough.

Target Market(s)

Home owners.

Colors

Designer to choose colors to be used in the design.

Requirements
Must have
• The same colours as my logo

```html
<!DOCTYPE html>
<html lang="en">
<head>
<meta charset="utf-8">
<title>Pelwick Builders – Trade Show Booth Set</title>
<link rel="stylesheet" href="https://fonts.googleapis.com/css2?family=Montserrat:wght@500;600;700;800&family=Oswald:wght@700&family=Cinzel:wght@700&display=swap">
<style>
  :root{
    --orange:#f0920a;
    --orange-deep:#d9800a;
    --navy:#0b1e2c;
    --sky:#3da3e6;
    --sky-light:#8fd0f5;
    --gray:#e4e4e4;
    --gray-light:#f1f1f1;
    --ink:#222;
    --text-dark:#3a3a3a;
    --white:#fff;
    --red-tab:#e85a24;
  }
  html,body{margin:0;padding:0;overflow:hidden;}
  body{background:var(--white);font-family:"Montserrat",sans-serif;}
  .canvas{position:relative;width:1200px;height:3507px;overflow:hidden;background:var(--white);}
  .abs{position:absolute;}
  .center{text-align:center;}
  .section-title{position:absolute;left:0;width:1200px;text-align:center;font-weight:700;font-size:27px;letter-spacing:.5px;color:var(--ink);}

  /* brand name block */
  .brand{position:absolute;display:flex;align-items:center;justify-content:center;gap:12px;font-family:"Montserrat",sans-serif;font-weight:800;letter-spacing:1px;white-space:nowrap;}
  .brand .mark{display:inline-block;flex:none;background:var(--orange);}

  /* wall box */
  .box-flap{background:var(--gray-light);}
  .box-side{background:linear-gradient(135deg,#ececec 0%,#d9d9d9 50%,#eeeeee 100%);}
  .box-photo{background:linear-gradient(180deg,#3a4a63 0%,#8a5a3a 45%,#3b3a2c 80%,#26261f 100%);}
  .box-band{background:linear-gradient(90deg,var(--orange-deep),var(--orange) 50%,var(--orange-deep));}
  .headline{font-family:"Oswald",sans-serif;font-weight:700;color:var(--white);text-transform:uppercase;}
  .service-strip{background:var(--orange);color:var(--white);font-weight:600;font-size:14px;line-height:18px;display:flex;flex-direction:column;justify-content:center;}
  .thumb{border:2px solid var(--orange);box-sizing:border-box;}
  .phone{display:flex;align-items:center;justify-content:center;gap:10px;color:var(--white);font-weight:700;}
  .phone svg{flex:none;}
  .url{color:var(--white);font-weight:500;}

  /* banners */
  .services-tab{background:var(--orange);color:var(--white);font-weight:800;font-size:33px;padding-left:51px;box-sizing:border-box;line-height:53px;clip-path:polygon(0 0,100% 0,88% 100%,0 100%);}
  .services-list{margin:0;padding:0;list-style:none;}
  .service-item{position:absolute;left:247px;font-weight:700;font-size:26px;line-height:31px;color:var(--navy);}
  .service-item::before{content:"»";position:absolute;left:-28px;color:var(--orange);font-weight:800;}
  .appointment{background:var(--orange);color:var(--white);font-family:"Oswald",sans-serif;font-weight:700;font-size:54px;line-height:68px;text-align:center;}
  .remodel-line{font-weight:800;color:var(--white);text-align:center;}
  .vacation{font-family:"Cinzel",serif;font-weight:700;color:var(--white);font-size:50px;line-height:46px;letter-spacing:3px;text-align:center;}

  /* table pieces */
  .tag-bar{background:var(--orange);color:var(--white);font-size:11px;font-weight:600;text-align:center;white-space:nowrap;}
  .faint-name{font-weight:800;color:#26352f;letter-spacing:2px;white-space:nowrap;}
</style>
</head>
<body>
<div class="canvas">

  <!-- ========== WALL BOX ========== -->
  <div class="section-title" style="top:88px;">10X8_FEET_WALL_BOX</div>

  <div class="abs box-flap" style="left:256px;top:177px;width:690px;height:93px;"></div>
  <div class="abs box-side" style="left:165px;top:270px;width:873px;height:409px;"></div>
  <div class="abs" style="left:266px;top:278px;width:670px;height:124px;border:1px solid #c9c9c9;border-bottom:none;box-sizing:border-box;"></div>
  <div class="abs box-photo" role="img" aria-label="Photo of a suburban street of houses at sunset" style="left:256px;top:402px;width:690px;height:277px;"></div>
  <div class="abs box-band" style="left:165px;top:679px;width:873px;height:143px;"></div>
  <div class="abs" style="left:256px;top:822px;width:690px;height:92px;background:var(--orange);"></div>

  <div class="brand" style="left:256px;top:330px;width:690px;height:50px;font-size:34px;color:#555;">
    <span class="mark" style="width:26px;height:26px;"></span>PELWICK BUILDERS
  </div>

  <div class="abs headline center" style="left:256px;top:414px;width:690px;font-size:60px;line-height:70px;">Roofing Done Right</div>
  <div class="abs service-strip center" style="left:370px;top:484px;width:460px;height:48px;">
    <span>Roofing • Siding • Windows &amp; Doors • Fiber Cement Siding</span>
    <span>Wood Siding • Gutter • Guards • Garage Doors</span>
  </div>

  <div class="abs thumb" role="img" aria-label="Photo of a shingle roof" style="left:372px;top:589px;width:137px;height:111px;background:linear-gradient(160deg,#6f8fa8,#5d5d58 60%,#3f4a3a);"></div>
  <div class="abs thumb" role="img" aria-label="Photo of an eavestrough on a house" style="left:532px;top:589px;width:136px;height:111px;background:linear-gradient(160deg,#5d84c8,#e8ecf0 55%,#50608a);"></div>
  <div class="abs thumb" role="img" aria-label="Photo of a house gable with siding" style="left:691px;top:589px;width:139px;height:111px;background:linear-gradient(160deg,#6fa2d8,#a58a72 50%,#e8d6a8);"></div>

  <div class="abs phone" style="left:256px;top:708px;width:690px;height:48px;font-size:39px;">
    <svg width="30" height="30" viewBox="0 0 24 24"><circle cx="12" cy="12" r="10.5" fill="none" stroke="currentColor" stroke-width="2"/><path d="M8.5 6.5l2 2-1.2 1.6a7 7 0 0 0 4.6 4.6l1.6-1.2 2 2-1.5 1.8c-4.5-.3-8.8-4.6-9.1-9.1z" fill="currentColor"/></svg>
    877-555-0148
  </div>
  <div class="abs url center" style="left:256px;top:755px;width:690px;font-size:20px;letter-spacing:4px;">www.pelwickbuilders.ca</div>

  <!-- ========== ROLL-UP BANNERS ========== -->
  <div class="section-title" style="top:982px;">ROLLUP_BANNER_STAND_2.5X6_FT (2)</div>

  <!-- Services banner -->
  <div class="abs" style="left:165px;top:1084px;width:402px;height:966px;background:var(--gray);overflow:hidden;">
    <div class="abs" style="left:0;top:0;width:402px;height:205px;background:linear-gradient(180deg,#44a8ea,#3a95d8);"></div>
    <div class="abs" role="img" aria-label="Photo of a row of houses with grey siding" style="left:0;top:205px;width:402px;height:201px;background:linear-gradient(180deg,#3e90d0 0%,#6f7f8c 30%,#8b8f8a 65%,#3b4a2f 100%);"></div>
    <div class="abs services-tab" style="left:0;top:379px;width:301px;height:53px;">SERVICES</div>
    <div class="abs" style="left:0;top:788px;width:402px;height:178px;background:linear-gradient(135deg,var(--orange-deep),var(--orange));"></div>
    <div class="abs" style="left:10px;top:10px;width:382px;height:946px;border:1px solid rgba(0,0,0,.25);box-sizing:border-box;"></div>
  </div>
  <div class="brand" style="left:165px;top:1200px;width:402px;height:60px;font-size:30px;color:var(--white);gap:10px;">
    <span class="mark" style="width:22px;height:22px;"></span>PELWICK BUILDERS
  </div>
  <ul class="services-list">
    <li class="service-item" style="top:1541px;">Roofing Services</li>
    <li class="service-item" style="top:1585px;">Roof Eavestrough<br>Services</li>
    <li class="service-item" style="top:1653px;">Windows &amp; Doors</li>
    <li class="service-item" style="top:1693px;">Siding Repairs &amp;<br>Installation</li>
    <li class="service-item" style="top:1762px;">Wood Siding</li>
    <li class="service-item" style="top:1806px;">Fiber Cement Siding</li>
  </ul>
  <div class="abs phone" style="left:165px;top:1898px;width:402px;height:52px;font-size:40px;">
    <svg width="32" height="32" viewBox="0 0 24 24"><circle cx="12" cy="12" r="10.5" fill="none" stroke="currentColor" stroke-width="2"/><path d="M8.5 6.5l2 2-1.2 1.6a7 7 0 0 0 4.6 4.6l1.6-1.2 2 2-1.5 1.8c-4.5-.3-8.8-4.6-9.1-9.1z" fill="currentColor"/></svg>
    877-555-0148
  </div>
  <div class="abs url center" style="left:165px;top:1947px;width:402px;font-size:22px;">www.pelwickbuilders.ca</div>

  <!-- Vacation banner -->
  <div class="abs" style="left:659px;top:1084px;width:402px;height:966px;overflow:hidden;">
    <div class="abs" style="left:0;top:0;width:402px;height:300px;background:linear-gradient(180deg,#2d8fd8,var(--sky-light));"></div>
    <div class="abs" role="img" aria-label="Photo of a traveller in a sun hat on a boat bow near tropical islands" style="left:0;top:300px;width:402px;height:352px;background:linear-gradient(180deg,#a9dcf3 0%,#5e8f6a 25%,#2fb3c0 50%,#7a6f62 80%,#5a5048 100%);"></div>
    <div class="abs" style="left:0;top:652px;width:402px;height:136px;background:var(--orange);"></div>
    <div class="abs" style="left:0;top:788px;width:402px;height:178px;background:var(--navy);"></div>
    <div class="abs" style="left:10px;top:10px;width:382px;height:946px;border:1px solid rgba(255,255,255,.35);box-sizing:border-box;"></div>
  </div>
  <div class="abs remodel-line" style="left:659px;top:1142px;width:402px;font-size:45px;line-height:47px;">BOOK YOUR<br>REMODEL</div>
  <div class="abs appointment" style="left:695px;top:1245px;width:329px;height:68px;">APPOINTMENT</div>
  <div class="abs remodel-line" style="left:659px;top:1305px;width:402px;font-size:78px;line-height:86px;">TODAY</div>
  <div class="abs vacation" style="left:659px;top:1762px;width:402px;">VACATION<br>TOMORROW</div>
  <div class="abs phone" style="left:659px;top:1894px;width:402px;height:52px;font-size:39px;">
    <svg width="32" height="32" viewBox="0 0 24 24"><circle cx="12" cy="12" r="10.5" fill="none" stroke="currentColor" stroke-width="2"/><path d="M8.5 6.5l2 2-1.2 1.6a7 7 0 0 0 4.6 4.6l1.6-1.2 2 2-1.5 1.8c-4.5-.3-8.8-4.6-9.1-9.1z" fill="currentColor"/></svg>
    877-555-0148
  </div>
  <div class="abs url center" style="left:659px;top:1943px;width:402px;font-size:22px;">www.pelwickbuilders.ca</div>

  <!-- ========== STRETCH TABLE COVER ========== -->
  <div class="section-title" style="top:2112px;">4_FEET_3-SIDED-STRETCH-TABLE-COVER</div>

  <svg class="abs table-cover" style="left:136px;top:2182px;" width="927" height="764" viewBox="100 1600 680 560" aria-label="Table cover template">
    <g fill="var(--navy)" stroke="var(--white)" stroke-width="5">
      <path d="M322,1618 L338,1618 Q342,1752 440,1754 Q538,1752 542,1618 L558,1618 L583,1800 L297,1800 Z"/>
      <path d="M297,1800 L137,1822 L137,1946 L297,1968 Z"/>
      <path d="M583,1800 L743,1822 L743,1946 L583,1968 Z"/>
      <path d="M297,1968 L583,1968 L560,2125 L320,2125 Z"/>
    </g>
    <g fill="none" stroke="#9a9a9a" stroke-width="1">
      <path d="M320,1616 L336,1616 Q340,1756 440,1758 Q540,1756 544,1616 L560,1616"/>
      <path d="M297,1800 L583,1800 M297,1968 L583,1968"/>
    </g>
    <rect x="297" y="1800" width="286" height="168" fill="var(--navy)"/>
    <rect x="115" y="1820" width="18" height="128" fill="var(--red-tab)" stroke="#555" stroke-width="1"/>
    <rect x="747" y="1820" width="18" height="128" fill="var(--red-tab)" stroke="#555" stroke-width="1"/>
    <rect x="321" y="2130" width="238" height="20" fill="var(--red-tab)" stroke="#555" stroke-width="1"/>
    <text x="440" y="2144" text-anchor="middle" font-family="Montserrat, sans-serif" font-size="8" fill="#222">3 BLEED</text>
  </svg>
  <div class="abs center faint-name" style="left:405px;top:2540px;width:390px;font-size:52px;line-height:60px;">PELWICK</div>
  <div class="brand" style="left:425px;top:2752px;width:350px;height:40px;font-size:27px;color:var(--white);gap:10px;">
    <span class="mark" style="width:19px;height:19px;"></span>PELWICK BUILDERS
  </div>
  <div class="abs tag-bar" style="left:506px;top:2836px;width:188px;height:20px;line-height:20px;">www.pelwickbuilders.ca</div>

  <!-- ========== ROUND FITTED TABLE ========== -->
  <div class="section-title" style="top:2998px;">ROUND-FITTED-TABLE-31.5X43</div>

  <div class="abs" style="left:64px;top:3091px;width:322px;height:322px;border-radius:50%;background:var(--navy);"></div>
  <div class="abs center faint-name" style="left:64px;top:3226px;width:322px;font-size:44px;">PELWICK</div>

  <div class="abs" style="left:424px;top:3104px;width:715px;height:296px;background:var(--navy);"></div>
  <div class="brand" style="left:424px;top:3220px;width:715px;height:50px;font-size:36px;color:var(--white);">
    <span class="mark" style="width:26px;height:26px;"></span>PELWICK BUILDERS
  </div>
  <div class="abs tag-bar" style="left:655px;top:3324px;width:253px;height:25px;line-height:25px;font-size:14px;">www.pelwickbuilders.ca</div>

</div>
</body>
</html>
```